Borvel Stake Pool, redesign of existing website

Borvel is a stake pool that allow its users to stake their Marevo crypto to yearn stable yields. The existing site is at www.borvelstake.org The site is today is a little dull and I want to have suggestions for a redesign that makes the site stand out and that picks up the colors of the logo. I am not looking for a complete redesign, mainly colors and smaller changes to layout. Examples of sites to be inspired by www.quenda.network, https://app.tervalo.finance/

Target Market(s)

Crypto users on Marevo

Number of Pages Required

1 page

```html
<!DOCTYPE html>
<html lang="en">
<head>
<meta charset="utf-8">
<title>Borvel Stake — Liquid Staking on Marevo</title>
<link rel="stylesheet" href="https://fonts.googleapis.com/css2?family=Alegreya:wght@700;800&family=Poppins:wght@400;500&display=swap">
<style>
:root{
  --bg:#111827;
  --panel:#131b2e;
  --line:#c9ccd3;
  --teal:#12a1a5;
  --orange:#f26a0f;
  --white:#ffffff;
  --field:#e8e8e8;
  --ink:#111111;
}
*{box-sizing:border-box;margin:0;padding:0}
html,body{width:1200px;height:3783px;overflow:hidden;background:var(--bg)}
body{position:relative;font-family:"Poppins",sans-serif;color:var(--white)}
.abs{position:absolute}
.serif{font-family:"Alegreya",serif;font-weight:700}
.brand{display:flex;align-items:center;gap:12px;font-family:"Alegreya",serif;font-weight:700;color:var(--white)}
.brand-dot{width:24px;height:24px;border-radius:50%;background:var(--teal)}
.nav a{position:absolute;top:40px;font-size:14px;color:var(--white);text-decoration:none}
.btn{position:absolute;display:flex;align-items:center;justify-content:center;border-radius:999px;color:var(--white)}
.btn-teal{background:var(--teal)}
.btn-orange{background:var(--orange)}
.btn-outline{border:1.5px solid var(--teal)}
.panel{position:absolute;border:1.5px solid var(--line);border-radius:32px;background:var(--panel)}
.hero-text{font-size:15.5px;line-height:28.5px}
.field{position:absolute;left:200px;width:800px;height:59px;border-radius:30px;background:var(--field);color:var(--ink);display:flex;align-items:center;padding:0 22px;font-size:22px;font-weight:500}
.field .amt{margin-left:auto;font-weight:400;font-size:22px;color:#333}
.token{width:28px;height:28px;border-radius:50%;margin-right:10px}
.small{font-size:13px}
.card{position:absolute;top:1816px;width:326px;height:402px;border:1.5px solid var(--line);border-radius:26px;padding:170px 26px 0}
.card p{font-size:17px;line-height:35.5px;font-weight:500}
.card svg{position:absolute;left:26px;top:32px}
.footer h4{position:absolute;top:3532px;font-size:15px;font-weight:400}
.footer a{position:absolute;font-size:14px;color:var(--white);text-decoration:none}
</style>
</head>
<body>

<header class="nav">
  <div class="brand abs" style="left:82px;top:40px;font-size:24px"><span class="brand-dot"></span>Borvel Stake</div>
  <a style="left:725px" href="#">Home</a>
  <a style="left:808px" href="#">Validators</a>
  <a style="left:920px" href="#">Docs</a>
  <div class="btn btn-teal" style="left:996px;top:36px;width:129px;height:33px;font-size:13.5px">Select Wallet</div>
</header>

<section class="hero">
  <h1 class="abs serif" style="left:75px;top:245px;font-size:62px;line-height:1">Liquid Staking on Marevo</h1>
  <p class="abs hero-text" style="left:77px;top:344px;width:600px">Borvel Stake Pool offers non-custodial staking. Stake your MRV to receive a liquid staking token, borvelMRV, that you can use in Defi on Marevo.<br>Let us take care of managing your stake across the best validators on Marevo, and your staking rewards will be automatically compounded each epoch. The value of borvelMRV relative to MRV will increase every epoch.</p>
  <div class="btn btn-teal" style="left:75px;top:533px;width:163px;height:56px;font-size:17px">Stake Now</div>
  <div class="abs" role="img" aria-label="Illustration of three coins flowing into a blue vault" style="left:749px;top:181px;width:376px;height:421px;border-radius:24px;background:linear-gradient(180deg,#f7a524 0%,#f7a524 24%,#1d4fb8 26%,#2f6fe0 70%,#4a4a4a 100%);opacity:.9"></div>
</section>

<section class="panel" style="left:75px;top:767px;width:1049px;height:730px">
</section>
<div class="btn btn-teal" style="left:200px;top:839px;width:254px;height:72px;font-size:22px">Stake</div>
<div class="btn btn-outline" style="left:473px;top:839px;width:253px;height:72px;font-size:22px">Unstake</div>
<div class="btn btn-outline" style="left:746px;top:839px;width:254px;height:72px;font-size:22px">Referral</div>
<p class="abs" style="left:0;width:1200px;top:970px;text-align:center;font-size:22px">Current APY: 8.03% across 60 validators</p>

<div class="field" style="top:1072px"><span class="token" style="background:#111"></span>MRV<span class="amt">0</span></div>
<p class="abs small" style="left:229px;top:1146px">balance: 0 MRV</p>
<p class="abs small" style="left:914px;top:1146px">max half</p>
<svg class="abs" style="left:571px;top:1147px" width="50" height="50" viewBox="0 0 50 50">
  <circle cx="25" cy="25" r="24" fill="#e8e8e8" stroke="#8a93a6" stroke-width="2"/>
  <path d="M25 14v20M17 27l8 8 8-8" fill="none" stroke="#111" stroke-width="2.5" stroke-linecap="round" stroke-linejoin="round"/>
</svg>
<div class="field" style="top:1225px"><span class="token" style="background:#f0503a"></span>borvelMRV<span class="amt">0</span></div>
<p class="abs small" style="left:233px;top:1300px">balance: 0 borvelMRV</p>
<p class="abs small" style="left:830px;top:1300px">1 borvelMRV = 1.01714 MRV</p>
<div class="btn btn-orange" style="left:450px;top:1371px;width:301px;height:73px;font-size:24px">Connect Wallet</div>

<section>
  <h2 class="abs serif" style="left:0;width:1200px;top:1600px;text-align:center;font-size:62px;line-height:72px"><span style="color:var(--teal)">Why Staking With Us</span><br>Helps You</h2>
  <div class="card" style="left:78px">
    <svg width="88" height="82" viewBox="0 0 88 82"><rect x="2" y="52" width="12" height="28" fill="#e0651b"/><rect x="22" y="42" width="12" height="38" fill="#f2a93b"/><rect x="42" y="48" width="12" height="32" fill="#e0651b"/><rect x="62" y="34" width="12" height="46" fill="#12a1a5"/><path d="M2 40 26 18 44 32 80 4" fill="none" stroke="#12a1a5" stroke-width="4"/><path d="M66 4h14v14" fill="none" stroke="#12a1a5" stroke-width="4"/></svg>
    <p>Get high yield returns similar to native staking, typically in the range 7-8% APY. The current APY is shown on https://bor-velstake.org.</p>
  </div>
  <div class="card" style="left:441px">
    <svg width="90" height="90" viewBox="0 0 90 90"><circle cx="45" cy="45" r="38" fill="none" stroke="#e0651b" stroke-width="3" stroke-dasharray="14 6"/><circle cx="45" cy="45" r="26" fill="none" stroke="#12a1a5" stroke-width="3"/><path d="M33 45l9 9 16-18" fill="none" stroke="#12a1a5" stroke-width="4"/></svg>
    <p>Be sure that you are supporting decentralization of the Marevo network. Borvel spreads your staked MRV to the best (and most decentralized) validators on Marevo.</p>
  </div>
  <div class="card" style="left:798px">
    <svg width="96" height="96" viewBox="0 0 96 96"><circle cx="30" cy="56" r="9" fill="none" stroke="#e0651b" stroke-width="4"/><path d="M39 56h50M36 48l30-28M36 64l30 24M30 47V8M70 10l18-6" stroke="#12a1a5" stroke-width="2.5" fill="none"/><circle cx="66" cy="20" r="4" fill="#12a1a5"/><circle cx="89" cy="56" r="4" fill="#12a1a5"/><circle cx="66" cy="88" r="4" fill="#12a1a5"/><circle cx="30" cy="8" r="4" fill="#e0651b"/></svg>
    <p>Participate in Defi. When you stake with Borvel you receive a liquid staking token (borvelMRV) that increases in value relative to MRV every epoch</p>
  </div>
</section>

<section class="panel" style="left:75px;top:2314px;width:1049px;height:448px"></section>
<div class="abs" role="img" aria-label="Gold star coin" style="left:218px;top:2368px;width:78px;height:96px;border-radius:50% 50% 50% 50%/40% 40% 60% 60%;background:radial-gradient(circle at 50% 65%,#f7a524 0 45%,#e57d14 46% 70%,transparent 71%)"></div>
<div class="abs" role="img" aria-label="Gold star coin" style="left:903px;top:2368px;width:78px;height:96px;border-radius:50% 50% 50% 50%/40% 40% 60% 60%;background:radial-gradient(circle at 50% 65%,#f7a524 0 45%,#e57d14 46% 70%,transparent 71%)"></div>
<h2 class="abs serif" style="left:0;width:1200px;top:2388px;text-align:center;font-size:84px;line-height:1;font-weight:800">EARN POINTS</h2>
<p class="abs" style="left:190px;width:820px;top:2515px;text-align:center;font-size:13.5px;line-height:28.5px">The Borvel Points Program is live! When you stake on Borvel you earn points. Hold it or earn even more points when using your borvelMRV with our defi partners. The amount of points determines what your allocation will be for our future governance token BVL. Leaderboard will be available soon!</p>
<div class="btn btn-orange" style="left:486px;top:2651px;width:228px;height:67px;font-size:18px">Stake Now</div>

<section>
  <div class="abs" role="img" aria-label="Photo of a hand touching a glowing blue DEFI interface" style="left:75px;top:2898px;width:432px;height:426px;border-radius:34px;background:radial-gradient(circle at 50% 50%,#2f7fd8 0%,#153a6b 45%,#0b1830 100%)"></div>
  <h2 class="abs serif" style="left:607px;top:2930px;font-size:56px;color:var(--teal)">Defi integrations</h2>
  <p class="abs" style="left:612px;top:3024px;width:500px;font-size:14px;line-height:26px">The borvel liquid staking token, borvelMRV, can be used on the following Defi applications. We are constantly evaluating new integrations, so if you are missing an integration that you would like to see, please let us know!</p>
  <div class="btn btn-outline" style="left:608px;top:3167px;width:166px;height:57px;font-size:17px">Liquidity</div>
  <div class="btn btn-outline" style="left:792px;top:3167px;width:188px;height:57px;font-size:17px">Borrow &amp; Lending</div>
  <div class="btn btn-outline" style="left:1003px;top:3167px;width:113px;height:57px;font-size:17px">Other</div>
</section>

<footer class="footer">
  <div class="brand abs" style="left:82px;top:3524px;font-size:30px"><span class="brand-dot" style="width:30px;height:30px"></span>Borvel Stake</div>
  <span class="abs" aria-label="Social link" style="left:182px;top:3607px;width:30px;height:30px;border-radius:50%;border:2px solid var(--teal)"></span>
  <h4 style="left:350px">OVERVIEW</h4>
  <a style="left:355px;top:3579px">Welcome</a>
  <a style="left:355px;top:3607px">Points Program</a>
  <h4 style="left:519px">LIQUID STAKING</h4>
  <a style="left:524px;top:3579px">What is Liquid Staking?</a>
  <a style="left:524px;top:3607px">Defi integrations</a>
  <h4 style="left:745px">VALIDATORS</h4>
  <a style="left:749px;top:3579px">Delegation Strategy</a>
  <a style="left:749px;top:3607px">Governance</a>
  <a style="left:749px;top:3635px">The BVL token</a>
  <h4 style="left:946px">NEWSLETTER SIGNUP</h4>
  <p class="abs" style="left:950px;top:3577px;font-size:14px;line-height:28px">Subscribe Our Newsletter<br>to get latest updates</p>
  <div class="abs" style="left:952px;top:3647px;width:172px;height:33px;background:#fff;display:flex;align-items:center;padding:3px">
    <span style="flex:1;height:100%;background:#dfe3f0;color:#556;font-size:9px;display:flex;align-items:center;padding-left:12px">Email Address</span>
    <span style="background:#111827;color:#fff;font-size:10px;height:100%;display:flex;align-items:center;padding:0 7px">Sign Up</span>
  </div>
  <div class="abs" style="left:75px;top:3719px;width:1049px;height:1px;background:#3a4358"></div>
  <p class="abs" style="left:0;width:1200px;top:3742px;text-align:center;font-size:12px">Copyright © 2024 All Rights Reserved By Company name</p>
</footer>

</body>
</html>
```